依頼詳細
人形町だけではなく、銀座でも配布予定のため、少しの高級感と親しみやすさを併せ持つようなデザインを希望いたします。
また、ローストチキンを思わず、注文したくなるようなチラシを作成していただきたいです。
記載項目
https://pagenoa.com/landing_pages/view/xq7m4
サイズ
A6
ページ数
片面
希望イメージ
シンプル 複雑
単色 カラフル
暗い 明るい
日常 高級
遊び心 厳粛
未来的 伝統的
女性的 男性的
希望する色
青系
納品ファイル
• 高解像度JPG (.jpg)
• イラストレーター形式 (.ai)
• フォトショップ形式 (.psd)
• PNG形式 (.png)
補足説明
店舗URL:https://www.lune-toki.com/

当方の想定していたイメージに最も合ったデザインを作成いただけました。

この度はご提案いただきありがとうございました。
当方の想定していたイメージに最も合ったデザインを作成いただけましたので、こちらを採用させていただきました。
また今後も機会がありましたらよろしくお願いいたします。
ありがとうございました。

```html
<!DOCTYPE html>
<html lang="ja">
<head>
<meta charset="utf-8">
<title>Bistro LUNE ローストチキン</title>
<link rel="stylesheet" href="https://fonts.googleapis.com/css2?family=Noto+Sans+JP:wght@400;700;900&family=Noto+Serif+JP:wght@700;900&family=Great+Vibes&family=Oswald:wght@500;700&display=swap">
<style>
:root{
  --navy:#1d2f5c;
  --navy-deep:#141f3d;
  --red:#d4202c;
  --gold:#d9b25a;
  --ink:#222;
  --paper:#ffffff;
  --tri-blue:#1f4aa8;
}
*{margin:0;padding:0;box-sizing:border-box}
html,body{width:855px;height:1200px;overflow:hidden;background:var(--paper)}
.flyer{position:relative;width:855px;height:1200px;background:var(--paper);font-family:"Noto Sans JP",sans-serif;color:var(--ink);overflow:hidden}
.tagline-band{position:absolute;top:0;left:0;width:100%;height:48px;background:var(--navy);color:#fff;font-family:"Noto Serif JP",serif;font-weight:700;font-size:24px;letter-spacing:4px;text-align:center;line-height:48px}
.tricolor{position:absolute;top:48px;left:0;width:100%;height:8px;display:flex}
.tricolor span{flex:1}
.tricolor .b{background:var(--tri-blue)}.tricolor .w{background:#fff}.tricolor .r{background:var(--red)}
.brand{position:absolute;top:78px;left:40px;display:flex;align-items:center;gap:12px;color:var(--navy);font-family:"Oswald",sans-serif;font-weight:700;font-size:54px;letter-spacing:2px}
.brand .dot{width:40px;height:40px;border-radius:50%;background:var(--navy)}
.title{position:absolute;top:62px;left:330px;color:var(--red);font-family:"Noto Sans JP",sans-serif;font-weight:900;font-size:76px;line-height:1.02;letter-spacing:2px}
.title .second{display:block;padding-left:40px}
.limit-badge{position:absolute;top:64px;left:712px;width:120px;height:120px;border-radius:50%;background:var(--red);color:#fff;text-align:center;font-weight:900;display:flex;flex-direction:column;justify-content:center;line-height:1.05}
.limit-badge .small{font-size:22px}
.limit-badge .big{font-size:34px}
.headline{position:absolute;top:226px;left:40px;color:var(--navy);font-family:"Noto Serif JP",serif;font-weight:900;font-size:34px;line-height:1.3}
.lead{position:absolute;top:318px;left:40px;width:780px;font-size:20px;font-weight:700;line-height:1.6;color:var(--ink)}
.details{position:absolute;top:460px;left:40px;width:380px;list-style:none;font-size:18px;font-weight:700;line-height:1.55;color:var(--ink)}
.details li::before{content:"● ";color:var(--navy)}
.details .indent{padding-left:20px}
.extras{position:absolute;top:450px;left:440px;width:400px}
.extras .plus{position:absolute;left:0;top:0;width:46px;height:46px}
.extras .plus::before,.extras .plus::after{content:"";position:absolute;background:var(--gold)}
.extras .plus::before{left:17px;top:0;width:12px;height:46px}
.extras .plus::after{left:0;top:17px;width:46px;height:12px}
.extras .note{margin-left:62px;font-size:16px;font-weight:700;color:var(--navy);line-height:1.35}
.extras ul{list-style:none;margin-top:12px;font-size:14px;font-weight:700;line-height:1.7}
.extras li{white-space:nowrap}
.extras li::before{content:"● ";color:var(--red)}
.night{position:absolute;top:660px;left:0;width:100%;height:460px;background:linear-gradient(180deg,var(--navy) 0%,var(--navy-deep) 100%)}
.chicken-photo{position:absolute;top:620px;left:300px;width:560px;height:480px;border-radius:48% 42% 40% 50%;background:radial-gradient(ellipse at 45% 40%,#e6a24a 0%,#b8661f 45%,#6d3410 80%,rgba(40,20,10,0) 100%)}
.chef-figure{position:absolute;top:930px;left:690px;width:130px;height:150px;border-radius:50% 50% 40% 40%;background:rgba(255,255,255,.18)}
.season{position:absolute;left:50px;top:900px;color:var(--gold);font-family:"Great Vibes",cursive;font-size:110px;line-height:1}
.season .year{display:block;font-family:"Oswald",sans-serif;font-size:44px;letter-spacing:6px;padding-left:120px;margin-top:6px}
.footer{position:absolute;bottom:0;left:0;width:100%;height:80px;background:var(--paper);display:flex;align-items:center;justify-content:center;gap:34px;color:var(--navy)}
.footer .shop{font-family:"Oswald",sans-serif;font-weight:700;font-size:38px;letter-spacing:1px}
.footer .shop small{font-size:22px;font-weight:500;margin-right:6px}
.footer .tel{font-family:"Oswald",sans-serif;font-weight:700;font-size:40px;letter-spacing:1px}
.footer .tel svg{vertical-align:-4px;margin-right:6px}
</style>
</head>
<body>
<div class="flyer">
  <div class="tagline-band">トリュフ香るきのこのバターライスとともに</div>
  <div class="tricolor"><span class="b"></span><span class="w"></span><span class="r"></span></div>

  <div class="brand"><span class="dot"></span>LUNE</div>
  <h1 class="title">ロースト<span class="second">チキン</span></h1>
  <div class="limit-badge"><span class="small">1日</span><span class="big">30羽</span><span class="small">限定</span></div>

  <h2 class="headline">ル・ギド星付きの<br>フレンチレストラン出身のシェフが作る</h2>
  <p class="lead">ローストチキンを食べて、贅沢なクリスマスのひと時を過ごしませんか？<br>中にはトリュフがふわっと香るきのこのバターライスがたっぷり。<br>しっとりジューシーで、ローストチキンってこんなに美味しいの?!と思える逸品です。<br>取りに来ていただく時間に合わせて、熱々で焼きたてをご提供します！</p>

  <ul class="details">
    <li>価格：4,000円（税別）</li>
    <li>予約期間：11/10〜12/15まで</li>
    <li>販売期間：12/20(金)〜25(水)</li>
    <li>受け取り時間：17:00または18:00</li>
    <li>受け取り店舗<br><span class="indent">ビストロ LUNE（人形町）or</span><br><span class="indent">ソル・エ・ルナ（恵比寿）</span></li>
  </ul>

  <div class="extras">
    <span class="plus"></span>
    <p class="note">チキンに加え、<br>いつもよりもっと特別な日にしたい方へ</p>
    <ul>
      <li>オードブルセット（全4品）+2000円（税別）</li>
      <li>選べる1ボトルセット（泡、白、赤）+8000円（税別）</li>
    </ul>
  </div>

  <div class="night"></div>
  <div class="chicken-photo" role="img" aria-label="こんがり焼き上がった丸ごとのローストチキンの写真"></div>
  <div class="chef-figure" role="img" aria-label="「C'est délicieux」と添えられたシェフの小さなイラスト"></div>
  <div class="season">X'mas<span class="year">2019</span></div>

  <div class="footer">
    <div class="shop"><small>Bistro</small>LUNE</div>
    <div class="tel"><svg width="30" height="30" viewBox="0 0 24 24" aria-hidden="true"><path fill="currentColor" d="M6.6 10.8a15.1 15.1 0 0 0 6.6 6.6l2.2-2.2a1 1 0 0 1 1-.25 11.4 11.4 0 0 0 3.6.57 1 1 0 0 1 1 1V20a1 1 0 0 1-1 1A17 17 0 0 1 3 4a1 1 0 0 1 1-1h3.5a1 1 0 0 1 1 1c0 1.250.2 2.45.57 3.57a1 1 0 0 1-.25 1z"/></svg>TEL:03-6000-4172</div>
  </div>
</div>
</body>
</html>
```